Website Design for a High School

School Name: Bayt Qamarin Private Schools
sub-schools:
1-Bayt Qamarin Primary School
2-Bayt Qamarin High School for Girls
3-Bayt Qamarin High School for Boys
The design should be professional and serious and below is the details of the website.
Pages: (Home, About Us, Schools, Events, Students, Gallery, Lectures, Contact Us).
A-) Home Page:
1-Animated photos banner as main
2-Marquee for the last news.
3-Welcoming block of text
4-latest news at the body of the page.
5-Calender "on the side"
6-Number of visitors "on the side"
7-Search bar
8-options to choose a school
B-) School Page:
three schools listed as drop down menu when highlighted over the Schools button in the menu
*Each school page should contain:
1-Student login area
2-Animation photos header
3-Specific news and projects
C-) Student Login page:
have a Report Card
D-) Gallery Page
have a collection of photos.
E-)Contact Page
phone numbers
emails
feedback form
F-)Other mentioned pages
with normal text and photos page look as similar to the Home page.
Required color: Purple as main and include the logo colors
Logo: is attached.
Button link to change language to Arabic.

```html
<!DOCTYPE html>
<html lang="en">
<head>
<meta charset="utf-8">
<title>Bayt Qamarin Private Schools</title>
<link href="https://fonts.googleapis.com/css2?family=Arimo:wght@400;700&family=Open+Sans:wght@800&display=swap" rel="stylesheet">
<style>
:root{
  --purple:#6c3fa3;
  --purple-dark:#5b3190;
  --yellow:#fde08a;
  --yellow-line:#f0c960;
  --text:#555;
  --muted:#888;
  --line:#d8d8d8;
  --bg:#f3f3f3;
  --white:#fff;
}
*{margin:0;padding:0;box-sizing:border-box}
html,body{width:1200px;height:1175px;overflow:hidden}
body{position:relative;background:var(--bg);font-family:"Arimo",Arial,sans-serif;color:var(--text)}
.abs{position:absolute}
.topbar{left:0;top:0;width:1200px;height:19px;background:var(--yellow)}
.lang{right:238px;top:4px;font-size:9px;color:#777;letter-spacing:.3px}
.lang b{font-weight:400;color:var(--purple);margin-left:8px}
.header{left:0;top:19px;width:1200px;height:118px;background:var(--white)}
.brand-mark{left:260px;top:35px;width:87px;height:87px;border-radius:50%;background:var(--yellow);border:5px solid var(--purple-dark)}
.site-title{left:363px;top:50px;font-size:23px;font-weight:700;color:var(--purple);letter-spacing:.2px}
.header-rule{left:363px;top:85px;width:598px;height:1px;background:var(--line)}
.nav a{position:absolute;top:97px;font-size:9.5px;color:#555;text-decoration:none;letter-spacing:.2px}
.nav-sep{left:942px;top:94px;width:1px;height:15px;background:var(--line)}
.search-ico{left:949px;top:96px}
.hero{left:0;top:137px;width:1200px;height:321px;background:radial-gradient(ellipse at 45% 40%,#5c6163 0%,#2f3436 55%,#1e2224 100%)}
.hero-title{left:0;top:314px;width:1220px;text-align:center;font-family:"Open Sans",Arial,sans-serif;font-weight:800;font-size:23px;color:#fff;letter-spacing:.4px}
.dots{left:597px;top:415px;display:flex;gap:4px}
.dots i{width:7px;height:7px;border-radius:50%;background:#fff}
.ticker{left:0;top:458px;width:1200px;height:38px;background:#f7f7f7;border-bottom:1px solid #e3e3e3}
.ticker-label{left:259px;top:473px;font-size:10px;color:#666}
.ticker-label b{color:var(--purple)}
.ticker-text{left:334px;top:474px;font-size:8.5px;color:#555}
.cal-card{left:258px;top:526px;width:237px;height:341px;background:var(--yellow);border:1px solid var(--yellow-line)}
.cal-head{left:274px;top:546px;font-size:15px;color:#333;display:flex;align-items:center;gap:7px}
.day-panel{left:273px;top:572px;width:93px;height:137px;background:var(--purple);color:#fff;text-align:center}
.day-name{margin-top:12px;font-size:10px;font-weight:700}
.day-num{font-size:56px;line-height:1;margin-top:8px}
.day-event{font-size:8.5px;line-height:13px;margin-top:10px}
.month-panel{left:366px;top:572px;width:113px;height:137px;background:#fff}
.month-title{position:absolute;left:28px;top:12px;font-size:8.5px;font-weight:700;color:var(--purple)}
.month-grid{position:absolute;left:4px;top:34px;width:105px;display:grid;grid-template-columns:repeat(7,15px);row-gap:4px;font-size:8px;text-align:center;color:#444}
.month-grid .dh{color:#e8a937;font-weight:700}
.month-grid .today{border:1.2px solid var(--purple);border-radius:50%;width:14px;height:14px;line-height:12px;margin:-2px auto 0}
.cal-rule{left:273px;top:724px;width:206px;height:1px;background:#e5c36a}
.visit-ico{left:366px;top:741px}
.visit-label{left:258px;top:767px;width:237px;text-align:center;font-size:11px;color:#333}
.visit-num{left:258px;top:782px;width:237px;text-align:center;font-size:42px;color:#fff}
.visit-sub{left:258px;top:824px;width:237px;text-align:center;font-size:11px;color:var(--purple)}
.search-field{left:509px;top:526px;width:225px;height:32px;background:#fff;border:1px solid #eee;font-size:10.5px;color:#f0c050;padding:10px 11px}
.search-field svg{position:absolute;right:9px;top:8px}
.school-select{left:739px;top:526px;width:222px;height:32px;background:#fff;font-size:10.5px;color:#bbb;padding:10px 15px}
.school-select svg{position:absolute;right:10px;top:13px}
.content{left:508px;top:562px;width:453px;height:501px;background:#fff;border:1px solid #e4e4e4}
.welcome{left:542px;top:589px;font-size:15px;color:#555}
.welcome b,.news-title b{color:var(--purple)}
.rule{height:1px;background:#ccc}
.body-copy{left:542px;top:623px;width:394px;font-size:8.6px;line-height:14px;color:#666}
.body-copy p{margin-bottom:14px}
.news-title{left:541px;top:881px;font-size:15px;color:#555}
.news-item{top:935px;display:flex;gap:10px}
.news-date{width:41px;height:39px;background:var(--yellow-line);color:#fff;text-align:center}
.news-date span{display:block;font-size:20px;line-height:22px;margin-top:2px}
.news-date small{display:block;font-size:9px}
.news-body{width:132px;font-size:8.6px;font-weight:700;color:#444;line-height:12px}
.news-body a{display:block;margin-top:6px;font-size:6.5px;font-weight:400;color:#999;text-decoration:underline}
.view-all{left:537px;top:1003px;width:72px;height:25px;border:1px solid #bbb;background:#fafafa;font-size:9px;font-weight:700;color:#555;text-align:center;line-height:23px;letter-spacing:.4px}
.footer{left:0;top:1099px;width:1200px;height:76px;background:#fff;border-top:1px solid #e3e3e3}
.copyright{left:259px;top:1127px;font-size:8.6px;color:#888}
</style>
</head>
<body>
<div class="abs topbar"></div>
<div class="abs lang">LANGUAGE: <b>EN | AR</b></div>

<header class="abs header"></header>
<div class="abs brand-mark"></div>
<h1 class="abs site-title">BAYT QAMARIN PRIVATE SCHOOLS</h1>
<div class="abs header-rule"></div>
<nav class="nav">
  <a style="left:363px">HOME</a>
  <a style="left:421px">ABOUT US</a>
  <a style="left:495px">SCHOOL</a>
  <a style="left:559px">EVENTS</a>
  <a style="left:618px">STUDENTS</a>
  <a style="left:689px">GALLERY</a>
  <a style="left:753px">LECTURERS</a>
  <a style="left:834px">CONTACT US</a>
</nav>
<div class="abs nav-sep"></div>
<svg class="abs search-ico" width="14" height="14" viewBox="0 0 14 14"><circle cx="5.5" cy="5.5" r="3.8" fill="none" stroke="#888" stroke-width="1.2"/><line x1="8.3" y1="8.3" x2="12.5" y2="12.5" stroke="#888" stroke-width="1.5"/></svg>

<div class="abs hero" role="img" aria-label="Banner photo: young student in graduation cap holding chalk before a blackboard"></div>
<div class="abs hero-title">SPIRITUAL GROWTH &amp; ACADEMIC EXCELLENCE</div>
<div class="abs dots"><i></i><i></i><i></i></div>

<div class="abs ticker"></div>
<div class="abs ticker-label">LATEST <b>NEWS</b></div>
<div class="abs ticker-text">Duis aute irure dolor in reprehenderit in voluptate velit esse cillum dolore eu fugiat nulla pariatur. Excepteur sint occaecat cupidatat</div>

<aside class="abs cal-card"></aside>
<div class="abs cal-head">
  <svg width="14" height="14" viewBox="0 0 14 14"><rect x="1" y="2.5" width="12" height="10.5" fill="none" stroke="#333" stroke-width="1.3"/><rect x="1" y="2.5" width="12" height="3" fill="#333"/><line x1="4" y1="1" x2="4" y2="4" stroke="#333" stroke-width="1.3"/><line x1="10" y1="1" x2="10" y2="4" stroke="#333" stroke-width="1.3"/><path d="M3.5 8h2M6.5 8h2M9.5 8h1M3.5 10.5h2M6.5 10.5h2" stroke="#333"/></svg>
  Calender
</div>
<div class="abs day-panel">
  <svg style="position:absolute;left:8px;top:13px" width="6" height="9" viewBox="0 0 6 9"><path d="M5 1L1 4.5 5 8" fill="none" stroke="#fff" stroke-width="1.2"/></svg>
  <div class="day-name">WEDNESDAY</div>
  <div class="day-num">20</div>
  <div class="day-event"><b>My Birthday</b><br>Event Text Here</div>
</div>
<div class="abs month-panel">
  <div class="month-title">MAY 20, 2015</div>
  <svg style="position:absolute;right:7px;top:13px" width="6" height="9" viewBox="0 0 6 9"><path d="M1 1l4 3.5L1 8" fill="none" stroke="#777" stroke-width="1.2"/></svg>
  <div class="month-grid">
    <span class="dh">S</span><span class="dh">M</span><span class="dh">T</span><span class="dh">W</span><span class="dh">T</span><span class="dh">F</span><span class="dh">S</span>
    <span></span><span></span><span></span><span></span><span></span><span>1</span><span>2</span>
    <span>3</span><span>4</span><span>5</span><span>6</span><span>7</span><span>8</span><span>9</span>
    <span>10</span><span>11</span><span>12</span><span>13</span><span>14</span><span>15</span><span>16</span>
    <span>17</span><span>18</span><span>19</span><span class="today">20</span><span>21</span><span>22</span><span>23</span>
    <span>24</span><span>25</span><span>26</span><span>27</span><span>28</span><span>29</span><span>30</span>
    <span>31</span>
  </div>
</div>
<div class="abs cal-rule"></div>
<svg class="abs visit-ico" width="16" height="13" viewBox="0 0 16 13"><circle cx="5" cy="3.5" r="2.6" fill="#333"/><circle cx="11" cy="3.5" r="2.6" fill="#333"/><path d="M0 12c0-4 2-6 5-6s5 2 5 6zM6 12c0-4 2-6 5-6s5 2 5 6z" fill="#333"/></svg>
<div class="abs visit-label">Right Now</div>
<div class="abs visit-num">25</div>
<div class="abs visit-sub">active visitor</div>

<div class="abs search-field">Search Keyword
  <svg width="16" height="16" viewBox="0 0 16 16"><circle cx="6" cy="6" r="4.3" fill="none" stroke="#f0c050" stroke-width="1.6"/><line x1="9.3" y1="9.3" x2="14.5" y2="14.5" stroke="#f0c050" stroke-width="2.2"/></svg>
</div>
<div class="abs school-select">Select School
  <svg width="10" height="6" viewBox="0 0 10 6"><path d="M0 0h10L5 6z" fill="#bbb"/></svg>
</div>

<main class="abs content"></main>
<h2 class="abs welcome">Welcome to <b>Bayt Qamarin Private Schools</b></h2>
<div class="abs rule" style="left:542px;top:610px;width:394px"></div>
<div class="abs body-copy">
  <p>Lorem Ipsum is simply dummy text of the printing and typesetting industry. Lorem Ipsum has been the industry's standard dummy text ever since the 1500s, when an unknown printer took a galley of type and scrambled it to make a type specimen book. It has survived not only five centuries, but also the leap into electronic typesetting, remaining essentially unchanged. It was popularised in the 1960s with the release of Letraset sheets containing Lorem Ipsum passages, and more recently with desktop publishing software like Aldus PageMaker including versions of Lorem Ipsum.</p>
  <p>Lorem ipsum dolor sit amet, consectetur adipiscing elit, sed do eiusmod tempor incididunt ut labore et dolore magna aliqua. Ut enim ad minim veniam, quis nostrud exercitation ullamco laboris nisi ut aliquip ex ea commodo consequat.</p>
  <p>Duis aute irure dolor in reprehenderit in voluptate velit esse cillum dolore eu fugiat nulla pariatur. Excepteur sint occaecat cupidatat non proident, sunt in culpa qui officia deserunt mollit anim id est laborum.</p>
  <p>Lorem ipsum dolor sit amet, consectetur adipiscing elit, sed do eiusmod tempor incididunt ut labore et dolore magna aliqua.</p>
</div>
<h2 class="abs news-title">Latest <b>News</b></h2>
<div class="abs rule" style="left:541px;top:902px;width:395px"></div>
<article class="abs news-item" style="left:541px">
  <div class="news-date"><span>08</span><small>NOV</small></div>
  <div class="news-body">Duis aute irure dolor in reprehen-derit in voluptate velit esse cillum<a>READ MORE &rarr;</a></div>
</article>
<article class="abs news-item" style="left:758px">
  <div class="news-date"><span>08</span><small>NOV</small></div>
  <div class="news-body">Duis aute irure dolor in reprehen-derit in voluptate velit esse cillum<a>READ MORE &rarr;</a></div>
</article>
<div class="abs view-all">VIEW ALL</div>

<footer class="abs footer"></footer>
<div class="abs copyright">© 2015.&nbsp; Bayt Qamarin Private Schools.</div>
</body>
</html>
```